Stationery Design for Consulting Company
Orvel Partners
Creative Brief
Professional
Tomas Wenholt
Director
Orvel Partners LLC 48215 Ridgefern Road Dunmore, DE 19872 USA
tomas@orvel-advisory.com
www.orvel-advisory.com
Maybe just a larger logo in the middle unless you have better ideas. I'm open to suggestions.

```html
<!DOCTYPE html>
<html lang="en">
<head>
<meta charset="utf-8">
<title>Orvel Partners — Business Card</title>
<link href="https://fonts.googleapis.com/css2?family=Cinzel:wght@500&family=Roboto:wght@400;500&display=swap" rel="stylesheet">
<style>
  :root {
    --page: #e4e4e4;
    --card-dark: #2e2e2e;
    --card-light: #fbfbfb;
    --accent: #f5a623;
    --ink: #3a3a3a;
    --ink-soft: #6b6b6b;
    --rule: #c9c9c9;
  }
  * { box-sizing: border-box; margin: 0; padding: 0; }
  html, body { width: 1200px; height: 902px; overflow: hidden; }
  body {
    background: var(--page);
    font-family: "Roboto", Arial, sans-serif;
    position: relative;
  }
  .card {
    position: absolute;
    left: 290px;
    width: 620px;
    height: 354px;
    border-radius: 14px;
    overflow: hidden;
    box-shadow: 0 6px 18px rgba(0,0,0,.18);
  }
  .card--back { top: 72px; background: var(--card-dark); }
  .card--front { top: 476px; background: var(--card-light); }

  .brand {
    display: flex;
    align-items: center;
    gap: 12px;
    font-family: "Cinzel", Georgia, serif;
    font-weight: 500;
    color: var(--accent);
    white-space: nowrap;
  }
  .brand__mark { background: var(--accent); flex: none; }

  .card--back .brand {
    position: absolute;
    left: 50%; top: 50%;
    transform: translate(-50%, -50%);
    font-size: 40px;
  }
  .card--back .brand__mark { width: 30px; height: 30px; }

  .card--front .brand {
    position: absolute;
    left: 34px; top: 92px;
    font-size: 23px;
  }
  .card--front .brand__mark { width: 18px; height: 18px; }

  .divider {
    position: absolute;
    left: 336px; top: 44px;
    width: 1px; height: 196px;
    background: var(--rule);
  }
  .contact {
    position: absolute;
    left: 360px; top: 48px;
    color: var(--ink);
  }
  .contact__name { font-size: 21px; font-weight: 400; letter-spacing: .2px; }
  .contact__title {
    font-size: 9px; letter-spacing: 1.4px; color: var(--ink-soft);
    margin-top: 4px; text-transform: uppercase;
  }
  .contact__list { list-style: none; margin-top: 26px; }
  .contact__list li {
    display: flex; align-items: center; gap: 9px;
    font-size: 11px; color: var(--ink); height: 19px;
  }
  .contact__list svg { width: 11px; height: 11px; fill: var(--ink); flex: none; }

  .wave { position: absolute; left: 0; bottom: 0; width: 620px; height: 120px; }
</style>
</head>
<body>

<section class="card card--back" aria-label="Card back">
  <div class="brand"><span class="brand__mark"></span>Orvel Partners LLC</div>
</section>

<section class="card card--front" aria-label="Card front">
  <div class="brand"><span class="brand__mark"></span>Orvel Partners LLC</div>
  <div class="divider"></div>
  <div class="contact">
    <p class="contact__name">Tomas Wenholt</p>
    <p class="contact__title">Director</p>
    <ul class="contact__list">
      <li><svg viewBox="0 0 12 12"><path d="M3 1l2 2-1 1.5c.6 1.4 1.6 2.4 3 3L8.5 6.5l2 2L9 10.5C5 10 2 7 1.5 3z"/></svg>302 555 0148</li>
      <li><svg viewBox="0 0 12 12"><rect x="3" y="1" width="6" height="10" rx="1"/></svg>302 555 0172</li>
      <li><svg viewBox="0 0 12 12"><rect x="1" y="4" width="10" height="6" rx="1"/><rect x="3" y="1" width="6" height="3"/></svg>302 555 0193</li>
      <li><svg viewBox="0 0 12 12"><path d="M1 3h10v7H1z M1 3l5 4 5-4" /></svg>tomas@orvel-advisory.com</li>
      <li><svg viewBox="0 0 12 12"><circle cx="6" cy="6" r="5"/></svg>www.orvel-advisory.com</li>
    </ul>
  </div>
  <svg class="wave" viewBox="0 0 620 120" preserveAspectRatio="none" aria-hidden="true">
    <path d="M0 40 C160 20 300 70 420 60 C520 52 580 30 620 24 L620 120 L0 120 Z" fill="var(--accent)"/>
    <path d="M0 52 C160 34 300 82 420 72 C520 64 580 42 620 36 L620 120 L0 120 Z" fill="var(--card-light)"/>
    <path d="M0 62 C160 46 300 92 420 84 C520 76 580 56 620 50 L620 120 L0 120 Z" fill="var(--card-dark)"/>
  </svg>
</section>

</body>
</html>
```